Kelvoran Financial Web Design Contest

We would like for you to design a website for www.kelvoranfinancial.example. Kelvoran Financial is a CPA Firm offering accounting, auditing, and tax preparation services.

We would like to have a consistent feel with the logo, business card, envelope, and stationary designs that were created by another designer on ArtHive. Examples of each are attached. We would like the website to have a clean/modern style.

The website should include the following:

1. A general "Welcome" landing page
2. A "About the Company" page
3. A "Services Offered" page
4. A "Contact Us" form
5. A button for "Sign up for Newsletter"

Target Market(s)

Individuals and businesses that require accounting, auditing, and tax preparation services from a CPA.

Industry/Entity Type

Accounting

Coding

Number of Pages Required

Font styles to use
Other font styles liked:
• Trebuchet or similar

Requirements
Must have
• Consistent feel with logo and letterhead. The gray and blue bar on the letterhead should be incorporated into the website design.

```html
<!DOCTYPE html>
<html lang="en">
<head>
<meta charset="utf-8">
<title>Kelvoran Financial — Contacts</title>
<link href="https://fonts.googleapis.com/css2?family=Ubuntu:wght@400;500&family=Jost:wght@400;500&display=swap" rel="stylesheet">
<style>
  :root {
    --white: #ffffff;
    --navy: #112a5e;
    --navy-deep: #0d2660;
    --ink: #1f2a44;
    --grey: #7d7d7d;
    --rule: #e6e8ee;
    --logo-grey: #4a4a4a;
    --footer-faint: #2c4a88;
    --footer-line: #1d3a74;
    --pen-tone: 10, 14, 28;
  }
  * { margin: 0; padding: 0; box-sizing: border-box; }
  html, body { width: 1200px; height: 1011px; overflow: hidden; background: var(--navy); }
  .canvas { position: relative; width: 1200px; height: 1011px; background: var(--navy); font-family: "Ubuntu", "Trebuchet MS", sans-serif; }

  /* header */
  .site-header { position: absolute; left: 0; top: 0; width: 1200px; height: 148px; background: var(--white); }
  .nav-link { position: absolute; top: 67px; font-size: 16px; color: var(--grey); text-decoration: none; }
  .nav-link.is-active { color: var(--navy-deep); }
  .nav-sep { position: absolute; top: 64px; width: 1px; height: 26px; background: #d9d9d9; }

  .brand { position: absolute; left: 0; width: 1200px; text-align: center; }
  .brand-square { position: absolute; left: 50%; transform: translateX(-50%); border: 4px solid var(--logo-grey); }
  .brand-name { position: absolute; left: 0; width: 100%; text-align: center; font-family: "Ubuntu", sans-serif; font-weight: 500; letter-spacing: 0.4px; color: var(--navy-deep); }
  .brand-tagline { position: absolute; left: 0; width: 100%; text-align: center; font-family: "Ubuntu", sans-serif; color: var(--navy-deep); }

  .header-brand { top: 0; height: 148px; }
  .header-brand .brand-square { top: 24px; width: 56px; height: 56px; }
  .header-brand .brand-name { top: 84px; font-size: 17px; }
  .header-brand .brand-tagline { top: 106px; font-size: 10.5px; letter-spacing: 0.6px; }
  .header-brand .brand-rule { position: absolute; top: 104px; left: 474px; width: 252px; height: 1px; background: #b9c1d3; }

  /* section */
  .section-title { position: absolute; top: 172px; left: 0; width: 1200px; text-align: center; color: var(--white); font-size: 16px; font-weight: 500; }

  .contact-card { position: absolute; left: 199px; top: 218px; width: 772px; height: 436px; background: var(--white); font-family: "Jost", sans-serif; color: var(--ink); }
  .card-mark { position: absolute; left: 38px; top: 35px; width: 56px; height: 56px; border: 3px solid #3d5a95; }
  .card-name { position: absolute; left: 106px; top: 54px; font-family: "Ubuntu", sans-serif; font-size: 13px; font-weight: 500; color: #3d5a95; }
  .card-address { position: absolute; right: 334px; top: 45px; text-align: right; font-size: 10.5px; line-height: 14.5px; }
  .card-address b, .card-links b { color: var(--navy-deep); font-weight: 500; }
  .card-divider { position: absolute; left: 448px; top: 42px; width: 1px; height: 46px; background: #777; }
  .card-links { position: absolute; left: 461px; top: 45px; font-size: 10.5px; line-height: 14.5px; }
  .card-social { position: absolute; left: 700px; top: 35px; width: 37px; height: 53px; border: 1px solid #dedede; }

  .field-label { position: absolute; left: 40px; font-size: 12px; color: #555; }
  .field-line { position: absolute; left: 91px; width: 247px; height: 1px; background: var(--rule); }
  .field-area { position: absolute; left: 40px; top: 247px; width: 695px; height: 143px; border: 1px solid var(--rule); }

  .send-button { position: absolute; left: 468px; top: 709px; width: 255px; height: 61px; border: 1px solid var(--white); color: var(--white); font-size: 15px; font-weight: 500; display: flex; align-items: center; justify-content: center; }

  .pen-illustration { position: absolute; left: 752px; top: 560px; width: 370px; height: 255px;
    background: radial-gradient(ellipse 50% 38% at 50% 55%, rgba(var(--pen-tone), 0.55), rgba(var(--pen-tone), 0.25) 55%, rgba(var(--pen-tone), 0) 100%); }

  /* footer */
  .footer-rule { position: absolute; left: 0; top: 833px; width: 1200px; height: 1px; background: var(--footer-line); }
  .footer-link { position: absolute; top: 914px; font-size: 16px; color: var(--footer-faint); }
  .footer-brand { top: 868px; height: 100px; }
  .footer-brand .brand-square { top: 2px; width: 56px; height: 56px; border-color: var(--footer-faint); }
  .footer-brand .brand-name { top: 62px; font-size: 17px; color: var(--footer-faint); }
  .footer-brand .brand-tagline { top: 84px; font-size: 10.5px; letter-spacing: 0.6px; color: var(--footer-faint); }
</style>
</head>
<body>
<div class="canvas">

  <header class="site-header">
    <a class="nav-link" style="left:254px">General</a>
    <span class="nav-sep" style="left:333px"></span>
    <a class="nav-link is-active" style="left:357px">About</a>
    <span class="nav-sep" style="left:435px"></span>

    <div class="brand header-brand">
      <span class="brand-square"></span>
      <span class="brand-name">KELVORAN FINANCIAL, LLC</span>
      <span class="brand-rule"></span>
      <span class="brand-tagline">Accounting · Audit · Tax Services</span>
    </div>

    <span class="nav-sep" style="left:763px"></span>
    <a class="nav-link" style="left:783px">Services</a>
    <span class="nav-sep" style="left:865px"></span>
    <a class="nav-link" style="left:890px">Contacts</a>
  </header>

  <h1 class="section-title">Contacts</h1>

  <section class="contact-card">
    <span class="card-mark"></span>
    <span class="card-name">Kelvoran Financial</span>
    <div class="card-address">
      218 Larkmoor Street<br>
      Suite 410, Alderbrook, GA 30999<br>
      555.014.2287 : <b>P</b>
    </div>
    <span class="card-divider"></span>
    <div class="card-links">
      <b>E</b> : info@kelvoranfinancial.example<br>
      <b>W</b> : www.kelvoranfinancial.example<br>
      <b>F</b> : social.example/KelvoranFinancial
    </div>
    <span class="card-social"></span>

    <span class="field-label" style="top:161px">Name</span>
    <span class="field-line" style="top:171px"></span>
    <span class="field-label" style="top:188px">E-mail</span>
    <span class="field-line" style="top:198px"></span>
    <span class="field-label" style="top:223px">Message</span>
    <div class="field-area"></div>
  </section>

  <div class="send-button">Send message</div>

  <div class="pen-illustration" role="img" aria-label="Photo of a black fountain pen with gold trim and its cap lying diagonally"></div>

  <div class="footer-rule"></div>
  <span class="footer-link" style="left:267px">General</span>
  <span class="footer-link" style="left:369px">About</span>
  <div class="brand footer-brand">
    <span class="brand-square"></span>
    <span class="brand-name">KELVORAN FINANCIAL, LLC</span>
    <span class="brand-tagline">Accounting · Audit · Tax Services</span>
  </div>
  <span class="footer-link" style="left:796px">Services</span>
  <span class="footer-link" style="left:903px">Contacts</span>

</div>
</body>
</html>
```